Heron Freightlines needs Bussiness cards!

Our new trucking company needs business cards!
We need the same design with two different names and emails, everything else it's the same.
I have included our original logo so we can use it for the design.
Note: the logo to be used is the o e with the buffalo on the right side, next to the letters H and F.

Target Market(s)

Trucking, refrigerated transportation, freight

Industry/Entity Type

Business

Contact Information for Business Card

Card #1:
Marcus Tellwright
marcustellwright@heronfreightlines.example
1-844-555-0193
(956)555-0178
3817 W. Tarrow Ave.
Pharr, TX 78599
www.heronfreightlines.example

Card#2:
Orla Brennick
orla@heronfreightlines.example
1-844-555-0193
(956)555-0178
3817 W. Tarrow Ave.
Pharr, TX 78599
www.heronfreightlines.example

Font styles to use
Sans Serif

Colors
0655a3
ec1f27
ffffff

Requirements
Must have
• our logo
Nice to have
• roads on background,

```html
<!DOCTYPE html>
<html lang="en">
<head>
<meta charset="utf-8">
<title>Heron Freightlines — Business Cards</title>
<link rel="stylesheet" href="https://fonts.googleapis.com/css2?family=Arimo:wght@400;700&display=swap">
<style>
  :root {
    --backdrop: #3a332f;
    --card: #1d1d1f;
    --card-edge: #2a2a2d;
    --brand-red: #ec1f27;
    --brand-blue: #0655a3;
    --name-blue: #0b4f94;
    --ink: #f2f2f2;
    --divider: #55565a;
  }
  * { margin: 0; padding: 0; box-sizing: border-box; }
  html, body { width: 1200px; height: 787px; overflow: hidden; }
  body {
    background: var(--backdrop);
    font-family: "Arimo", Arial, sans-serif;
    position: relative;
  }
  .card {
    position: absolute;
    top: 233px;
    width: 560px;
    height: 320px;
    background: var(--card);
    border: 1px solid var(--card-edge);
    border-radius: 4px;
    box-shadow: 0 8px 24px rgba(0,0,0,.35);
  }
  .card--front { left: 30px; }
  .card--back { left: 610px; }

  .wordmark {
    display: flex;
    align-items: center;
    gap: 12px;
    color: var(--brand-red);
    font-weight: 700;
    line-height: 1;
  }
  .wordmark__dot {
    flex: none;
    border-radius: 50%;
    background: var(--brand-blue);
  }
  .wordmark__text { display: flex; flex-direction: column; }

  .card--front .wordmark {
    position: absolute;
    left: 70px;
    top: 88px;
    font-size: 44px;
  }
  .card--front .wordmark__dot { width: 46px; height: 46px; }
  .front-url {
    position: absolute;
    left: 42px;
    top: 238px;
    color: var(--ink);
    font-size: 14px;
    letter-spacing: 3.4px;
  }

  .card--back .wordmark {
    position: absolute;
    left: 26px;
    top: 118px;
    font-size: 29px;
  }
  .card--back .wordmark__dot { width: 30px; height: 30px; }
  .back-divider {
    position: absolute;
    left: 255px;
    top: 40px;
    width: 1px;
    height: 240px;
    background: var(--divider);
  }
  .contact {
    position: absolute;
    left: 272px;
    top: 58px;
    color: var(--ink);
    font-size: 13px;
    line-height: 1.3;
  }
  .contact__name {
    color: var(--name-blue);
    font-size: 19px;
    margin-bottom: 14px;
  }
  .contact__address { margin-bottom: 12px; }
  .contact__list { list-style: none; }
  .contact__item {
    display: flex;
    align-items: center;
    gap: 8px;
    height: 22px;
    white-space: nowrap;
  }
  .contact__item--small { font-size: 11.5px; }
  .contact__icon { width: 13px; height: 13px; flex: none; fill: var(--ink); }
</style>
</head>
<body>

<section class="card card--front" aria-label="Card front">
  <div class="wordmark">
    <span class="wordmark__dot"></span>
    <span class="wordmark__text"><span>Heron</span><span>Freightlines</span></span>
  </div>
  <p class="front-url">www.heronfreightlines.example</p>
</section>

<section class="card card--back" aria-label="Card back">
  <div class="wordmark">
    <span class="wordmark__dot"></span>
    <span class="wordmark__text"><span>Heron</span><span>Freightlines</span></span>
  </div>
  <span class="back-divider"></span>
  <div class="contact">
    <p class="contact__name">Marcus Tellwright</p>
    <p class="contact__address">3817 W. Tarrow Ave.<br>Pharr, TX 78599</p>
    <ul class="contact__list">
      <li class="contact__item">
        <svg class="contact__icon" viewBox="0 0 16 16" aria-hidden="true"><path d="M2 6c0-2 2-3 6-3s6 1 6 3v1h-3V5.5H5V7H2z"/><rect x="3" y="8" width="10" height="6" rx="1"/></svg>
        1-844-555-0193
      </li>
      <li class="contact__item">
        <svg class="contact__icon" viewBox="0 0 16 16" aria-hidden="true"><path d="M5 1h6a1 1 0 0 1 1 1v12a1 1 0 0 1-1 1H5a1 1 0 0 1-1-1V2a1 1 0 0 1 1-1zm0 2v9h6V3z"/></svg>
        (956)555-0178
      </li>
      <li class="contact__item contact__item--small">
        <svg class="contact__icon" viewBox="0 0 16 16" aria-hidden="true"><path d="M1 3h14v1.5L8 9 1 4.5z"/><path d="M1 6l7 4.5L15 6v7H1z"/></svg>
        marcustellwright@heronfreightlines.example
      </li>
      <li class="contact__item">
        <svg class="contact__icon" viewBox="0 0 16 16" aria-hidden="true"><circle cx="8" cy="8" r="7"/></svg>
        www.heronfreightlines.example
      </li>
    </ul>
  </div>
</section>

</body>
</html>
```